Label design for an exciting new Vodka brand

We need a label design for a dynamic new Vodka brand called 'Pale lantern Vodka'. It is a crisp and versatile liquid with a clean and smooth finish. It should appeal to 21-39 year olds, with a slight female skew. Colours, fonts and styles should be modern and relatively neutral - take inspiration from the brand pictures attached.

Target Market(s)

21-39 year olds, both male and female, but with a slight female skew

```html
<!DOCTYPE html>
<html lang="en">
<head>
<meta charset="utf-8">
<title>Pale Lantern Vodka – Label</title>
<link rel="stylesheet" href="https://fonts.googleapis.com/css2?family=Archivo+Black&family=Bitter:wght@500;700&family=Poppins:wght@600;700;800&display=swap">
<style>
  :root {
    --backdrop: #383838;
    --paper: #ffffff;
    --paper-shade: #e9e9e9;
    --ink: #101010;
    --brand-red: #9b0c0f;
    --brand-red-deep: #5a0407;
    --band-text: #ffffff;
  }
  html, body {
    margin: 0;
    padding: 0;
    width: 921px;
    height: 1200px;
    overflow: hidden;
    background: var(--backdrop);
  }
  .canvas {
    position: relative;
    width: 921px;
    height: 1200px;
  }
  .label {
    position: absolute;
    left: 40px;
    top: 192px;
    width: 841px;
    height: 815px;
  }
  .label__distillery, .label__original {
    font-family: "Bitter", Georgia, serif;
    font-weight: 500;
    fill: var(--ink);
  }
  .label__brand-main {
    font-family: "Archivo Black", "Arial Black", sans-serif;
    fill: var(--ink);
  }
  .label__brand-sub, .label__category, .label__flavor, .label__spec {
    font-family: "Poppins", Arial, sans-serif;
    font-weight: 700;
    fill: var(--ink);
  }
  .label__flavor { font-weight: 600; }
  .label__spec { fill: var(--band-text); }
</style>
</head>
<body>
<main class="canvas">
  <svg class="label" viewBox="0 0 841 815" xmlns="http://www.w3.org/2000/svg" aria-label="Pale Lantern Vodka label">
    <defs>
      <radialGradient id="paperTone" cx="0.5" cy="0.45" r="0.75">
        <stop offset="0" stop-color="var(--paper)"/>
        <stop offset="0.7" stop-color="#f6f6f6"/>
        <stop offset="1" stop-color="var(--paper-shade)"/>
      </radialGradient>
      <linearGradient id="bandTone" x1="0" y1="0" x2="1" y2="0">
        <stop offset="0" stop-color="#a00d10"/>
        <stop offset="0.24" stop-color="var(--brand-red-deep)"/>
        <stop offset="0.38" stop-color="#a50f12"/>
        <stop offset="0.52" stop-color="#8e0a0d"/>
        <stop offset="0.62" stop-color="var(--brand-red-deep)"/>
        <stop offset="0.76" stop-color="#a00d10"/>
        <stop offset="0.9" stop-color="#62050a"/>
        <stop offset="1" stop-color="#a00d10"/>
      </linearGradient>
    </defs>

    <!-- paper with torn top edge -->
    <path class="label__paper" fill="url(#paperTone)"
      d="M0 16 L14 18 L28 14 L44 20 L62 15 L80 21 L98 17 L118 22 L140 16 L160 19 L178 13 L196 11 L218 16 L240 13 L262 18 L286 14 L310 10 L334 15 L356 12 L380 17 L404 11 L426 8 L452 13 L478 9 L502 12 L526 7 L552 4 L578 9 L602 6 L628 10 L652 5 L676 3 L700 8 L724 5 L750 9 L776 6 L800 11 L822 9 L841 13 L841 815 L0 815 Z"/>

    <text class="label__distillery" x="420" y="94" text-anchor="middle" font-size="20" letter-spacing="9">DISTILLERY NAME</text>
    <text class="label__original" x="420" y="178" text-anchor="middle" font-size="16" letter-spacing="8" font-weight="700">100% ORIGINAL</text>

    <text class="label__brand-main" x="138" y="500" font-size="420" textLength="562" lengthAdjust="spacingAndGlyphs">PALE</text>

    <g class="label__stripes" fill="var(--brand-red)">
      <rect x="138" y="518" width="54" height="4"/><rect x="138" y="530" width="54" height="4"/>
      <rect x="138" y="542" width="54" height="4"/><rect x="138" y="554" width="54" height="4"/>
      <rect x="138" y="566" width="54" height="4"/><rect x="138" y="578" width="54" height="4"/>
      <rect x="646" y="518" width="54" height="4"/><rect x="646" y="530" width="54" height="4"/>
      <rect x="646" y="542" width="54" height="4"/><rect x="646" y="554" width="54" height="4"/>
      <rect x="646" y="566" width="54" height="4"/><rect x="646" y="578" width="54" height="4"/>
    </g>
    <text class="label__brand-sub" x="205" y="590" font-size="98" textLength="430" lengthAdjust="spacingAndGlyphs">LANTERN</text>

    <text class="label__category" x="420" y="637" text-anchor="middle" font-size="36" letter-spacing="34">VODKA</text>

    <g class="label__flavor-rules" fill="var(--brand-red)">
      <rect x="0" y="716" width="268" height="2"/><rect x="0" y="722" width="268" height="2"/>
      <rect x="574" y="716" width="267" height="2"/><rect x="574" y="722" width="267" height="2"/>
    </g>
    <text class="label__flavor" x="424" y="727" text-anchor="middle" font-size="19" letter-spacing="11">FLAVOR NAME</text>

    <rect class="label__band" x="0" y="738" width="841" height="77" fill="url(#bandTone)"/>
    <text class="label__spec" x="125" y="788" text-anchor="middle" font-size="29">80PROOF</text>
    <text class="label__spec" x="420" y="788" text-anchor="middle" font-size="29">500ML</text>
    <text class="label__spec" x="725" y="788" text-anchor="middle" font-size="29">40% ABV</text>
  </svg>
</main>
</body>
</html>
```